Recruitment Site Design

We need a design for the login page, about page, and inner pages of a recruitment site for an oil and gas company. Design should be modern, sleek, professional and colors can be blue, green, white, orange or any other recommended colors.

Please also take into consideration that once the users login, they will need to access a form to fill in their information.

** UPDATE: Kindly provide a design for the inner information page consistent with the outer design. Attached is a picture of the basic structure. ***
Updates

Please provide a design for inner pages as shown in the design brief consistent with the registration page provided. 

Reason: We're extending it to get more inside pages.

Target Market(s)

Professionals looking for a career in the oil and gas industry in the Middle East.

Industry/Entity Type

Oil And Gas

Requirements
Must have
• Sleek design

```html
<!DOCTYPE html>
<html lang="en">
<head>
<meta charset="utf-8">
<title>Recruitment – Home</title>
<link rel="stylesheet" href="https://fonts.googleapis.com/css2?family=Fira+Sans:wght@400;500&family=Fira+Sans+Condensed:wght@400&display=swap">
<style>
:root{
  --orange:#e5870f;
  --orange-dark:#b9650a;
  --logo:#e0800f;
  --panel:#f3f3f3;
  --panel-border:#d6d6d6;
  --nav-top:#4a4a4a;
  --nav-bottom:#1f1f1f;
  --text:#4a4a4a;
  --white:#ffffff;
  --ribbon-dark:#2e2e2e;
}
*{box-sizing:border-box;margin:0;padding:0}
html,body{width:1200px;height:931px;overflow:hidden;background:var(--white)}
body{position:relative;font-family:"Fira Sans",Arial,sans-serif;color:var(--text)}
.abs{position:absolute}

.header-panel{left:180px;top:0;width:842px;height:178px;background:var(--panel);border-radius:0 0 10px 10px;box-shadow:0 8px 10px -6px rgba(0,0,0,.18)}
.logo{left:0;width:1200px;top:28px;text-align:center;font-size:55px;font-weight:400;color:var(--logo);letter-spacing:-1px}
.nav-tail{top:100px}
.main-nav{left:170px;top:109px;width:860px;height:55px;background:linear-gradient(var(--nav-top),var(--nav-bottom));box-shadow:0 3px 4px rgba(0,0,0,.35)}
.main-nav a{position:absolute;top:17px;transform:translateX(-50%);color:var(--white);text-decoration:none;font-size:16px;font-family:"Fira Sans Condensed","Fira Sans",sans-serif;letter-spacing:.3px}
.main-nav a.current{color:var(--orange)}

.slider-frame{left:172px;top:202px;width:858px;height:364px;border:1px solid var(--panel-border);border-radius:10px;background:repeating-linear-gradient(45deg,#f1f1f1 0 2px,#e4e4e4 2px 3px);box-shadow:0 16px 14px -12px rgba(0,0,0,.3)}
.slider-photo{left:186px;top:214px;width:832px;height:335px;border-radius:5px;background:linear-gradient(90deg,#c9b9a6 0%,#e9e3da 30%,#e6edf5 45%,#7d98bd 62%,#98acc6 80%,#6b7b8c 100%)}
.slider-arrow{top:352px;width:38px;height:38px;border-radius:50%;background:radial-gradient(circle at 40% 35%,#fbfbfb,#d3d3d3);border:1px solid #bdbdbd;box-shadow:0 0 0 6px #f3f3f3,0 0 0 7px #d6d6d6}

.welcome-panel{left:183px;top:612px;width:557px;height:223px;background:var(--panel);border:1px solid var(--panel-border);border-radius:4px;box-shadow:0 10px 8px -8px rgba(0,0,0,.15)}
.welcome-title{left:207px;top:638px;font-family:"Fira Sans Condensed","Fira Sans",sans-serif;font-size:26px;color:var(--white)}
.welcome-body{left:207px;top:704px;width:520px;font-family:"Fira Sans Condensed","Fira Sans",sans-serif;font-size:17px;line-height:26.7px;color:var(--text)}

.login-panel{left:764px;top:611px;width:264px;height:222px;background:var(--panel);border:1px solid var(--panel-border);border-radius:6px;box-shadow:0 10px 8px -8px rgba(0,0,0,.15)}
.login-tab{left:805px;top:600px;width:184px;height:60px;background:var(--orange);border-radius:0 0 4px 4px;box-shadow:0 2px 3px rgba(0,0,0,.3);color:var(--white);text-align:center;padding-top:16px;font-family:"Fira Sans Condensed","Fira Sans",sans-serif;font-size:25px}
.field{left:789px;width:210px;height:38px;background:var(--white);border:1px solid #e2e2e2;border-radius:3px;padding:10px 8px;font-family:"Fira Sans Condensed","Fira Sans",sans-serif;font-size:15px;color:#555}
.btn{top:781px;height:31px;background:var(--orange);border-radius:2px;color:var(--white);text-align:center;padding-top:6px;font-family:"Fira Sans Condensed","Fira Sans",sans-serif;font-size:16px}

.social-ribbon{top:833px}
.site-footer{left:0;width:1246px;top:874px;text-align:center;font-family:"Fira Sans Condensed","Fira Sans",sans-serif;font-size:14px;line-height:20px;color:#444}
</style>
</head>
<body>

<svg class="abs nav-tail" style="left:116px" width="60" height="57" viewBox="0 0 60 57"><polygon points="0,0 60,0 60,57 0,57 30,28" fill="var(--ribbon-dark)"/></svg>
<svg class="abs nav-tail" style="left:1024px" width="60" height="57" viewBox="0 0 60 57"><polygon points="0,0 60,0 30,28 60,57 0,57" fill="var(--ribbon-dark)"/></svg>

<div class="abs header-panel"></div>
<div class="abs logo">Logo Here</div>

<nav class="abs main-nav">
  <a class="current" style="left:102px">Home</a>
  <a style="left:237px">About Us</a>
  <a style="left:388px">Find Job</a>
  <a style="left:554px">Register Here</a>
  <a style="left:736px">Contact Us</a>
</nav>

<div class="abs slider-frame"></div>
<div class="abs slider-photo" role="img" aria-label="Engineers in hard hats reviewing plans beside an oil pump jack under a cloudy blue sky"></div>
<div class="abs slider-arrow" style="left:153px"><svg width="38" height="38" viewBox="0 0 38 38"><path d="M27 19H12M17 13l-6 6 6 6" stroke="#777" stroke-width="3" fill="none" stroke-linecap="round" stroke-linejoin="round"/></svg></div>
<div class="abs slider-arrow" style="left:1012px"><svg width="38" height="38" viewBox="0 0 38 38"><path d="M11 19h15M21 13l6 6-6 6" stroke="#777" stroke-width="3" fill="none" stroke-linecap="round" stroke-linejoin="round"/></svg></div>

<section>
  <div class="abs welcome-panel"></div>
  <svg class="abs" style="left:140px;top:627px" width="335" height="86" viewBox="0 0 335 86">
    <polygon points="0,22 40,22 40,84 0,84 14,53" fill="var(--orange-dark)"/>
    <polygon points="29,0 333,0 310,30 333,59 29,59" fill="var(--orange)"/>
    <polygon points="29,59 43,59 43,84" fill="#8a4b08"/>
  </svg>
  <h1 class="abs welcome-title" style="font-weight:400">Welcome to our site</h1>
  <p class="abs welcome-body">We need a design for the login page, about page, and inner pages of a recruitment site for an oil and gas company. Design should be modern, sleek, professional and colors can be blue, green, white, orange or any other recommended colors.</p>
</section>

<section>
  <div class="abs login-panel"></div>
  <svg class="abs" style="left:790px;top:600px" width="214" height="12" viewBox="0 0 214 12"><polygon points="15,0 0,12 15,12" fill="var(--orange-dark)"/><polygon points="199,0 214,12 199,12" fill="var(--orange-dark)"/></svg>
  <h2 class="abs login-tab" style="font-weight:400">Login Here</h2>
  <div class="abs field" style="top:677px">User Name</div>
  <div class="abs field" style="top:728px">Password</div>
  <div class="abs btn" style="left:790px;width:78px">Login</div>
  <div class="abs btn" style="left:880px;width:119px">Register Here</div>
</section>

<svg class="abs social-ribbon" style="left:852px" width="46" height="75" viewBox="0 0 46 75"><polygon points="0,0 46,0 46,75 23,64 0,75" fill="var(--ribbon-dark)"/><circle cx="23" cy="33" r="8" fill="var(--white)"/></svg>
<svg class="abs social-ribbon" style="left:905px" width="46" height="75" viewBox="0 0 46 75"><polygon points="0,0 46,0 46,75 23,64 0,75" fill="var(--ribbon-dark)"/><circle cx="23" cy="33" r="8" fill="var(--white)"/></svg>

<footer class="abs site-footer">Copyright @ 2012, All rights reserved.<br>Terms &amp; Privacy Policy</footer>

</body>
</html>
```